Business card design needed

I need a business card for my private practice. I would like to see the designs that use bright blue and white. I would like to see similar designs as to the card below:
http://blog.printvarno.com/2009/designing-a-business-card-with-pv-ks517-template.html
I would like to see the back of the card have room for appointment times. Thank you.

Industry/Entity Type
Business
Contact Information for Business Card
Brightwater Counselling & Wellness Services
Helen Dorsey B.Psychology
Registered Psychologist
Building C, Level 3, 14 Marrow Crescent, Canberra, ACT 2601
T: (02) 6287 5912
F: (02) 6287 5930
info@brightwatercounselling.com.au
www.brightwatercounselling.com.au

```html
<!DOCTYPE html>
<html lang="en">
<head>
<meta charset="utf-8">
<title>Brightwater Counselling &amp; Wellness Services – Business Card</title>
<link href="https://fonts.googleapis.com/css2?family=Roboto:wght@300;400;500;700&display=swap" rel="stylesheet">
<style>
  :root {
    --stage: #1b1b1b;
    --blue-light: #0aa2cf;
    --blue-mid: #0873bd;
    --blue-deep: #0b4a9c;
    --brand-blue: #0a76b6;
    --card-white: #f7f8f9;
    --ink: #2e2e2e;
    --white: #ffffff;
  }
  * { margin: 0; padding: 0; box-sizing: border-box; }
  html, body {
    width: 1200px; height: 907px; overflow: hidden;
    background: var(--stage);
    font-family: "Roboto", Arial, sans-serif;
  }
  .stage { position: relative; width: 1200px; height: 907px; }

  .card { position: absolute; left: 272px; width: 656px; height: 378px; overflow: hidden; }

  /* Front */
  .card-front {
    top: 62px;
    background: radial-gradient(ellipse 70% 95% at 50% 0%, var(--blue-light) 0%, var(--blue-mid) 45%, var(--blue-deep) 100%);
  }
  .brand {
    position: absolute; display: flex; align-items: center; gap: 12px;
    font-weight: 700; line-height: 1.05;
  }
  .brand-dot { border-radius: 50%; flex: none; }
  .card-front .brand {
    left: 0; right: 0; top: 150px; justify-content: center;
    color: var(--white); font-size: 30px;
  }
  .card-front .brand-dot { width: 22px; height: 22px; background: var(--white); }
  .web-rule {
    position: absolute; left: 0; right: 0; top: 334px;
    display: flex; align-items: center; gap: 14px;
  }
  .web-rule .rule { flex: 1; height: 3px; background: var(--white); }
  .web-rule .url { color: var(--white); font-size: 17px; font-weight: 500; letter-spacing: 0.2px; }

  /* Back */
  .card-back { top: 467px; background: var(--card-white); }
  .card-back .brand {
    left: 46px; top: 54px; color: var(--brand-blue); font-size: 21px;
  }
  .card-back .brand-dot { width: 16px; height: 16px; background: var(--brand-blue); }
  .name-band {
    position: absolute; left: 359px; right: 0; top: 70px; height: 79px;
    background: var(--brand-blue); color: var(--white);
    padding: 18px 0 0 28px;
  }
  .name-band .name { font-size: 21px; font-weight: 400; }
  .name-band .credential { font-size: 14px; font-weight: 300; margin-top: 3px; }
  .contact {
    position: absolute; left: 48px; top: 192px;
    font-size: 14px; font-weight: 300; line-height: 22px; color: var(--ink);
    list-style: none;
  }
  .divider {
    position: absolute; left: 327px; top: 191px; width: 2px; height: 131px;
    background: var(--brand-blue);
  }
  .appointments {
    position: absolute; left: 386px; top: 192px;
    font-size: 14px; line-height: 22px; color: var(--ink);
  }
  .appointments h2 { font-size: 14px; font-weight: 500; }
  .appointments .field { display: flex; font-weight: 300; }
  .appointments .label { width: 92px; }
  .base-stripe {
    position: absolute; left: 0; right: 0; top: 346px; height: 7px;
    background: var(--brand-blue);
  }
  .card-back::after {
    content: ""; position: absolute; left: 0; right: 0; top: 353px; bottom: 0;
    background: var(--white);
  }
</style>
</head>
<body>
<main class="stage">
  <section class="card card-front" aria-label="Card front">
    <div class="brand">
      <span class="brand-dot"></span>
      <span>Brightwater Counselling<br>&amp; Wellness Services</span>
    </div>
    <div class="web-rule">
      <span class="rule"></span>
      <span class="url">www.brightwatercounselling.com.au</span>
      <span class="rule"></span>
    </div>
  </section>

  <section class="card card-back" aria-label="Card back">
    <div class="brand">
      <span class="brand-dot"></span>
      <span>Brightwater Counselling<br>&amp; Wellness Services</span>
    </div>
    <div class="name-band">
      <h1 class="name">Helen Dorsey</h1>
      <p class="credential">B.Psychology Registered</p>
    </div>
    <ul class="contact">
      <li>Psychologist Building C</li>
      <li>Level 3, 14 Marrow Crescent</li>
      <li>Canberra, ACT 2601</li>
      <li>T: (02) 6287 5912</li>
      <li>F: (02) 6287 5930</li>
      <li>info@brightwatercounselling.com.au</li>
    </ul>
    <span class="divider"></span>
    <div class="appointments">
      <h2>Appointment Schedule</h2>
      <p class="field"><span class="label">Date</span><span>:</span></p>
      <p class="field"><span class="label">Time</span><span>:</span></p>
    </div>
    <span class="base-stripe"></span>
  </section>
</main>
</body>
</html>
```